Hurricane Damage Public Adjuster Billboard

I have created several projects with you and have several great designs. I need to format them into a Billboard for upcoming Hurricane Season. Need done in a month. Im also in process of getting an eye catching and easy to remember 800# Vanity phone number like Call 800-Stormfix or 800- Need Help? My included past Sketch Guild projects will give you an idea of what colors, schemes, and designs I gravitate towards. 3 past Design projects were 1) 2 Logos where I picked the 1st place and the 2nd place and 2) Index Card where I picked the winner as the Index Card and the 2nd place as a Post Card. Point is, I will pick and pay for 2 winners if they're good. This should help to sweeten the pot. Also, please look at my website for ideas that I like:

www.TheClaimWardenGroup.com
I want people to feel that I am the best and highest. Level.

I've been getting a lot of quick half effort designs basically cut & pasting my previous projects. Please don't rush and take your time to be creative. A an example, my Biggest Competitor is Crestline Public Adjusting. Their colors are Black and Gold while mine are Blue, White, and Black with a highlight of Orange if possible. I JUST imported a picture of their BillBoard. I need mine better and BLOW AWAY THEIRS. Terms like "Don't be Victimized Twice ?, Don't let the Hurricane Ruin your Life?". "Get Fairly Paid & Move On" "Our Clients Claims are VIP?
Updates

I'm getting a lot of quick half effort ones. I'd rather you take your time and really put some thoughts and effort into it. My Biggest Competitor is Crestline Public Adjusting. They have black & gold colors, while I have Blue, Black, and white.

It needs to blow theirs away. I have imported their Billboard for comparative purposes.

Guy's,
I'll make it easier for you in what I'm looking for. Please look at the Crestline Billboard picture attached.

1) Put my "Blue Shield" to the left, replacing their logo
2) change color patterns from their (Black, Gold, White) to my color schemes of (Black, Blue, White)
3) I want to see my name where their is:

THE
Claim Warden Group
EXPERT & LOCAL Public Adjusters
"FOR THE POLICYHOLDER!!"

4) to the right, add the A+Rated logo and QTR+ Accredited logo, 5 Star Zentrio Rated logo, 5 Start BLOCKLINK Highly Rated logo, etc..

5) the right side is where you can be creative as I will not have a picture of me there.

"20+ Years of Experience, Recovering Millions for our VIP Clients"

"Your Best, Locally-Based Private Adjuster & Advocate'
"FOR THE POLICYHOLDER!!"

"Don't be victimized Twice!!"

"Don't let the Hurricane Ruin Your Life!!"

This should really help. Also, refer to my website, maybe a couple testimonial fillers?

Thanks all,

marvin@TheClaimWardenGroup.com

Just imported a few awards that would look great to the right side with all the other 5 Star Ratings and accolades.
This right section could be titled like zmy Website:

5 Star Reviews, Ratings & Awards:
4-5 Logos underneath?

Target Market(s)

Coastal place where a Hurricane 🌀 🌀 Hits

Industry/Entity Type

Hurricane Public Insurance Adjuster

Font styles to use
Sans Serif
Other font styles liked:
• Calvera fonts

Colors
0054AA
0677BA
7BADD7
CADEEF
E8F1F8
EE7325
F08F49
F5BC92
FAE3D3
FDF4ED

Requirements
Must have
• Use my past project logos, colors, and schemes to create eye grabbing BillBoard
Nice to have
Should not have
• Not be too busy, must be Easy to Read, Eye Catchy

```html
<!DOCTYPE html>
<html lang="en">
<head>
<meta charset="utf-8">
<title>Claim Warden Group Billboard</title>
<link href="https://fonts.googleapis.com/css2?family=Playfair+Display:wght@400&family=Great+Vibes&family=Oswald:wght@300;500;600&family=Montserrat:wght@500;700;800&family=Libre+Caslon+Text&display=swap" rel="stylesheet">
<style>
  :root {
    --blue-bright: #08c0f2;
    --blue-main: #0596d6;
    --blue-deep: #0677ba;
    --ink: #050505;
    --white: #ffffff;
    --red: #e8141c;
    --storm-dark: #0d1220;
    --storm-mid: #2a2f4a;
    --storm-glow: #7c6f8c;
    --page: #f2f2f2;
  }
  * { box-sizing: border-box; margin: 0; padding: 0; }
  html, body {
    width: 1189px; height: 1200px; overflow: hidden;
    background: var(--page);
  }
  .billboard {
    position: absolute; left: 40px; top: 439px;
    width: 1109px; height: 322px; overflow: hidden;
    background: linear-gradient(110deg, var(--blue-bright) 0%, var(--blue-main) 45%, var(--blue-deep) 100%);
  }
  .storm-scene {
    position: absolute; inset: 0;
    clip-path: polygon(780px 0, 1109px 0, 1109px 322px, 693px 322px);
    background:
      radial-gradient(ellipse 180px 90px at 920px 70px, var(--storm-glow) 0%, transparent 70%),
      radial-gradient(ellipse 160px 80px at 940px 180px, #6a4a3a 0%, transparent 75%),
      linear-gradient(180deg, var(--storm-mid) 0%, var(--storm-dark) 60%, #151a14 80%);
  }
  .ratings-band {
    position: absolute; left: 0; right: 0; bottom: 0; height: 70px;
    clip-path: polygon(708px 0, 1109px 0, 1109px 70px, 693px 70px);
    background: linear-gradient(180deg, rgba(0,0,0,0.6) 0%, var(--ink) 35%);
  }
  .brand {
    position: absolute; left: 40px; top: 95px; width: 230px;
    display: flex; align-items: center; gap: 12px;
  }
  .brand-square { width: 34px; height: 34px; background: var(--white); flex: none; }
  .brand-name {
    font-family: "Montserrat", sans-serif; font-weight: 800;
    font-size: 26px; line-height: 1.05; color: var(--white);
  }
  .headline {
    position: absolute; left: 318px; top: 20px; width: 360px;
    text-align: center; color: var(--white);
    font-family: "Playfair Display", serif; font-weight: 400;
    text-transform: uppercase; line-height: 0.95;
  }
  .headline .line { display: block; font-size: 38px; letter-spacing: -0.5px; }
  .headline .line-big { font-size: 52px; margin-top: 4px; }
  .headline .script {
    font-family: "Great Vibes", cursive; text-transform: none;
    color: var(--ink); font-size: 62px; margin-left: -4px;
  }
  .credential-box {
    position: absolute; left: 302px; top: 189px; width: 372px; height: 60px;
    border: 2px solid var(--white);
    display: flex; align-items: center; padding: 0 8px;
  }
  .credential-text {
    font-family: "Montserrat", sans-serif; font-weight: 500;
    font-size: 9.5px; line-height: 1.15; color: var(--white); width: 190px;
  }
  .credential-text strong { font-weight: 700; }
  .credential-arrow { width: 24px; height: 20px; margin: 0 12px 0 4px; }
  .adjuster-name {
    font-family: "Montserrat", sans-serif; font-weight: 800;
    font-size: 20px; line-height: 1; color: var(--white); text-align: center;
  }
  .call-bar {
    position: absolute; left: 14px; top: 270px; width: 340px; height: 42px;
    background: var(--ink);
    clip-path: polygon(0 0, 100% 0, 94% 100%, 0 100%);
    display: flex; align-items: center; padding-left: 18px;
    font-family: "Oswald", sans-serif; font-size: 30px; color: var(--white);
    letter-spacing: 0.5px;
  }
  .call-bar .light { font-weight: 300; margin-right: 9px; }
  .call-bar .number { font-weight: 600; }
  .web-bar {
    position: absolute; left: 346px; top: 270px; width: 352px; height: 42px;
    background: var(--white);
    clip-path: polygon(4% 0, 100% 0, 96% 100%, 0 100%);
    display: flex; align-items: center; padding-left: 22px;
    font-family: "Oswald", sans-serif; font-size: 25px; color: var(--ink);
  }
  .web-bar .light { font-weight: 300; }
  .web-bar .bold { font-weight: 600; }
  .rating {
    position: absolute; left: 722px; top: 262px; width: 170px; text-align: center;
  }
  .rating-title {
    font-family: "Montserrat", sans-serif; font-weight: 800;
    font-size: 28px; color: var(--red); line-height: 1;
  }
  .rating-sub {
    font-family: "Libre Caslon Text", serif; font-size: 10.5px;
    line-height: 1.1; color: var(--white); margin-top: 4px;
  }
  .badges {
    position: absolute; left: 914px; top: 268px;
    display: flex; gap: 5px; align-items: center;
  }
  .badge { background: var(--white); height: 40px; }
  .badge-wide { width: 84px; border-radius: 2px; }
  .badge-square { width: 42px; }
  .badge-small { width: 32px; height: 36px; background: #8aa0c0; }
</style>
</head>
<body>
  <section class="billboard">
    <div class="storm-scene" role="img" aria-label="Two-storey house lit at night under a stormy sky with lightning"></div>
    <div class="ratings-band"></div>

    <div class="brand">
      <span class="brand-square"></span>
      <span class="brand-name">Claim Warden Group</span>
    </div>

    <h1 class="headline">
      <span class="line">Don't let the</span>
      <span class="line">Hurricane ruin</span>
      <span class="line line-big">Your<span class="script">Life!!</span></span>
    </h1>

    <div class="credential-box">
      <p class="credential-text">THE<br>Claim Warden Group<br>EXPERT &amp; LOCAL Public Adjusters<br><strong>"FOR THE POLICYHOLDER!!"</strong></p>
      <svg class="credential-arrow" viewBox="0 0 24 20" aria-hidden="true">
        <polygon points="0,0 12,10 0,20" fill="#050505"/>
        <polygon points="11,0 23,10 11,20" fill="#050505"/>
      </svg>
      <p class="adjuster-name">MARVIN<br>HALVERSEN</p>
    </div>

    <div class="call-bar"><span class="light">CALL</span><span class="number">800-STORMFIX</span></div>
    <div class="web-bar"><span class="light">The</span><span class="bold">ClaimWardenGroup</span><span class="light">.com</span></div>

    <div class="rating">
      <p class="rating-title">A+ Rating</p>
      <p class="rating-sub">High Rating For<br>Public Insurance Adjusters</p>
    </div>

    <div class="badges">
      <span class="badge badge-wide"></span>
      <span class="badge badge-square"></span>
      <span class="badge badge-small"></span>
    </div>
  </section>
</body>
</html>
```